Presentation Flyer for Married Couple at night separate business owners by day

I would like a flyer to use to advertise free presentations put on by husband and I. I (Renata Volkhaven) am an estate planning attorney that works for PWR Law. My husband (Dan Volkhaven) is a financial planner that works for Quelmora Financial Planning. Would love it to be funny but serious. At night we are a married couple of 4 children, by day we individually work with people helping them protect their assets and their families.
Goal is for this to be used for multiple events.
Things to include: Food will be provided, Raffle for $500 off an Estate Plan Package
Topics to be covered in Seminar:
Estate & Financial Planning Essentials

Protect Your Future
Build a strong financial foundation with emergency funds, retirement planning, and smart investment strategies that match your goals.

Secure Your Legacy
Learn about wills, trusts, and powers of attorney - the essential documents everyone needs to protect their family's future.

Guard Your Assets
Understand the right insurance coverage to protect yourself and your loved ones, from life insurance to long-term care options.

Transfer Wealth Wisely
Discover tax-efficient strategies for passing assets to the next generation and making the most of your charitable giving.

```html
<!DOCTYPE html>
<html lang="en">
<head>
<meta charset="utf-8">
<title>Estate &amp; Financial Planning Essentials</title>
<link href="https://fonts.googleapis.com/css2?family=Lexend:wght@300;400;500;600&family=Manrope:wght@700;800&family=Outfit:wght@300;400&display=swap" rel="stylesheet">
<style>
  :root{
    --ink:#0a2230;
    --navy:#0d4a6b;
    --blue:#0b4f8a;
    --teal-dark:#0b4a68;
    --teal:#1593bd;
    --cyan:#52d3f5;
    --grey:#b3c2c8;
    --footer:#071c28;
    --white:#ffffff;
  }
  *{margin:0;padding:0;box-sizing:border-box}
  html,body{width:848px;height:1200px;overflow:hidden;background:var(--white)}
  body{font-family:"Lexend",sans-serif;color:var(--ink)}
  .flyer{position:relative;width:848px;height:1200px;overflow:hidden;background:var(--white)}
  .abs{position:absolute}
  .hero-shapes{left:0;top:0}
  .firm-name{left:60px;top:98px;font-family:"Lexend",sans-serif;font-weight:600;font-size:20px;color:var(--navy);letter-spacing:.5px}
  .title{left:55px;top:166px;font-family:"Manrope",sans-serif;font-weight:800;font-size:55px;line-height:56px;color:var(--ink);letter-spacing:-.3px}
  .presenters{left:57px;top:406px;font-family:"Lexend",sans-serif;font-weight:600;font-size:16.5px;color:var(--navy);letter-spacing:-.2px}
  .topics{left:0;top:478px;width:848px;height:353px;background:linear-gradient(100deg,var(--teal-dark) 0%,#0e6d91 55%,var(--teal) 100%)}
  .topics-heading{position:absolute;top:22px;width:100%;text-align:center;color:var(--white);font-family:"Lexend",sans-serif;font-weight:600;font-size:27px;letter-spacing:-.2px}
  .topic-card{position:absolute;top:112px;width:177px;height:221px;border:1px solid rgba(255,255,255,.28);border-radius:6px;background:rgba(255,255,255,.06);color:var(--white);text-align:center;padding:46px 4px 0}
  .topic-card h3{font-family:"Lexend",sans-serif;font-weight:500;font-size:17px;line-height:20.5px;margin-bottom:5px;white-space:nowrap}
  .topic-card p{font-family:"Outfit",sans-serif;font-weight:300;font-size:13.4px;line-height:19.2px}
  .topic-icon{position:absolute;top:-46px;left:50%;margin-left:-40px;width:80px;height:90px}
  .family-photo{left:0;top:831px}
  .partner-name{left:430px;top:852px;font-family:"Lexend",sans-serif;font-weight:600;font-size:30px;color:var(--ink)}
  .include-heading{left:427px;top:926px;font-family:"Lexend",sans-serif;font-weight:600;font-size:26px;color:var(--blue)}
  .include-text{left:429px;top:970px;width:310px;font-weight:400;font-size:19px;line-height:26px;color:var(--ink)}
  .include-text strong{font-weight:600}
  .phone-button{left:429px;top:1061px;width:208px;height:50px;border-radius:8px;background:linear-gradient(90deg,var(--teal-dark),var(--teal));display:flex;align-items:center;padding-left:14px;gap:10px;color:var(--white);font-weight:600;font-size:19px}
  .footer{left:0;top:1132px;width:848px;height:68px;background:var(--footer);color:var(--white);font-weight:300;font-size:15.5px}
  .footer-item{position:absolute;top:22px;display:flex;align-items:center;gap:8px}
</style>
</head>
<body>
<div class="flyer">

  <svg class="abs hero-shapes" width="848" height="478" viewBox="0 0 848 478">
    <defs>
      <linearGradient id="heroTone" x1="0" y1="0" x2="1" y2="1">
        <stop offset="0" stop-color="#c7a58f"/>
        <stop offset=".5" stop-color="#3d4556"/>
        <stop offset="1" stop-color="#1e2638"/>
      </linearGradient>
    </defs>
    <polygon points="0,375 30,354 30,443 0,456" fill="var(--grey)"/>
    <polygon points="429,0 848,0 848,350 620,478 429,478" fill="url(#heroTone)" role="img" aria-label="Photo of the two presenters, a smiling married couple seated together"/>
    <polygon points="396,0 660,0 396,147" fill="var(--blue)"/>
  </svg>

  <div class="abs firm-name">Quelmora Financial LLC</div>

  <h1 class="abs title">Estate &amp;<br>Financial<br>Planning<br>Essentials</h1>

  <div class="abs presenters">RENATA VOLKHAVEN | DAN VOLKHAVEN</div>

  <section class="abs topics">
    <h2 class="topics-heading">Topics to be covered in Seminar</h2>

    <div class="topic-card" style="left:57px">
      <svg class="topic-icon" viewBox="0 0 80 90"><polygon points="40,2 77,23 77,67 40,88 3,67 3,23" fill="var(--cyan)"/><path d="M40 28 L55 34 V46 C55 56 48 62 40 65 C32 62 25 56 25 46 V34 Z" fill="none" stroke="var(--teal-dark)" stroke-width="2.2"/><path d="M33 46 L38 51 L47 41" fill="none" stroke="var(--teal-dark)" stroke-width="2.2"/></svg>
      <h3>Protect Your<br>Future</h3>
      <p>Build a strong financial foundation with emergency funds, retirement planning, and smart investment strategies that match your goals.</p>
    </div>

    <div class="topic-card" style="left:243px">
      <svg class="topic-icon" viewBox="0 0 80 90"><polygon points="40,2 77,23 77,67 40,88 3,67 3,23" fill="var(--cyan)"/><g fill="none" stroke="var(--teal-dark)" stroke-width="2"><path d="M40 28 V62 M32 62 H48 M24 36 H56"/><path d="M24 36 L18 50 H30 Z M56 36 L50 50 H62 Z"/></g></svg>
      <h3>Secure Your<br>Legacy</h3>
      <p>Learn about wills, trusts, and powers of attorney - the essential documents everyone needs to protect their family's future.</p>
    </div>

    <div class="topic-card" style="left:429px">
      <svg class="topic-icon" viewBox="0 0 80 90"><polygon points="40,2 77,23 77,67 40,88 3,67 3,23" fill="var(--cyan)"/><g fill="none" stroke="var(--teal-dark)" stroke-width="2"><path d="M22 46 C22 34 30 28 40 28 C50 28 58 34 58 46 Z"/><path d="M40 46 V60 C40 64 34 64 34 60"/></g></svg>
      <h3>Guard Your<br>Assets</h3>
      <p>Understand the right insurance coverage to protect yourself and your loved ones, from life insurance to long-term care options.</p>
    </div>

    <div class="topic-card" style="left:615px">
      <svg class="topic-icon" viewBox="0 0 80 90"><polygon points="40,2 77,23 77,67 40,88 3,67 3,23" fill="var(--cyan)"/><g fill="none" stroke="var(--teal-dark)" stroke-width="2"><path d="M28 44 L40 34 L52 44 V58 H28 Z"/><path d="M37 58 V50 H43 V58"/></g></svg>
      <h3>Transfer Wealth<br>Wisely</h3>
      <p>Discover tax-efficient strategies for passing assets to the next generation and making the most of your charitable giving.</p>
    </div>
  </section>

  <svg class="abs family-photo" width="381" height="301" viewBox="0 0 381 301">
    <defs>
      <linearGradient id="familyTone" x1="0" y1="0" x2="1" y2="1">
        <stop offset="0" stop-color="#e8d6c8"/>
        <stop offset=".5" stop-color="#c99a80"/>
        <stop offset="1" stop-color="#6f88a8"/>
      </linearGradient>
    </defs>
    <polygon points="100,0 360,0 360,301 0,301 0,59" fill="url(#familyTone)" role="img" aria-label="Photo of a happy family of three hugging outdoors"/>
    <polygon points="381,214 381,301 225,301" fill="var(--blue)"/>
  </svg>

  <div class="abs partner-name">PWR Law</div>

  <h2 class="abs include-heading">Things to include</h2>
  <p class="abs include-text">Food will be provided, Raffle for <strong>$500</strong> off an Estate Plan Package</p>

  <div class="abs phone-button">
    <svg width="34" height="34" viewBox="0 0 34 34"><circle cx="17" cy="17" r="17" fill="var(--cyan)"/><path d="M11 9 L15 9 L16 14 L13.5 15.5 C14.5 18 16 19.5 18.5 20.5 L20 18 L25 19 L25 23 C25 24 24 25 23 25 C15 24.5 9.5 19 9 11 C9 10 10 9 11 9 Z" fill="var(--teal-dark)"/></svg>
    <span>+123-456-7890</span>
  </div>

  <footer class="abs footer">
    <div class="footer-item" style="left:64px">
      <svg width="18" height="22" viewBox="0 0 18 22"><path d="M9 0 C4 0 0 4 0 9 C0 15 9 22 9 22 C9 22 18 15 18 9 C18 4 14 0 9 0 Z" fill="var(--cyan)"/><circle cx="9" cy="9" r="3.2" fill="var(--footer)"/></svg>
      <span>123 Anywhere St., Any City</span>
    </div>
    <div class="footer-item" style="left:342px">
      <svg width="20" height="20" viewBox="0 0 20 20"><circle cx="10" cy="10" r="8.5" fill="none" stroke="var(--cyan)" stroke-width="2.2"/><path d="M1.5 10 H18.5 M10 1.5 C6 6 6 14 10 18.5 M10 1.5 C14 6 14 14 10 18.5" fill="none" stroke="var(--cyan)" stroke-width="1.6"/></svg>
      <span>www.website.com</span>
    </div>
    <div class="footer-item" style="left:552px">
      <svg width="20" height="15" viewBox="0 0 20 15"><rect x="0" y="0" width="20" height="15" rx="1.5" fill="var(--cyan)"/><path d="M1 1.5 L10 9 L19 1.5" fill="none" stroke="var(--footer)" stroke-width="1.6"/></svg>
      <span>hello@website.com</span>
    </div>
  </footer>

</div>
</body>
</html>
```